Business card for Property Management consultant

I need a business card for my business LX Vantage - I consult to real estate agents to improve the performance of their Property Management departments (rental houses management). The card needs to be very professional looking, incorporating our logo and my photo plus the line "Develop your Rent Roll to Perform"

Target Market(s)

Real Estate business owners

Industry/Entity Type

Business Consultant

Contact Information for Business Card

Business name - LX Vantage (logo uploaded)
My Name : Marlene Okafor -
Title : Property Management Consultant

Develop your Rent Roll to perform

Phone : +61 438902716
email : marlene@lxvantage.com.au
website ; www.lxvantage.com.au

Requirements
Must have
• Logo
• My photo
• Very corporate / professional look

```html
<!DOCTYPE html>
<html lang="en">
<head>
<meta charset="utf-8">
<title>LX Vantage – Business Card</title>
<link rel="stylesheet" href="https://fonts.googleapis.com/css2?family=Questrial&family=Open+Sans:wght@400;700&display=swap">
<style>
  :root {
    --page-bg: #e9eaec;
    --brand-blue: #25489a;
    --brand-blue-light: #3560b8;
    --brand-blue-dark: #1c3a82;
    --sky: #2fa3dc;
    --gold: #c8952f;
    --ink: #1d1d1f;
    --rule-grey: #b9bcc2;
    --white: #ffffff;
    --photo-top: #d9dde4;
    --photo-bottom: #3f68b8;
  }
  * { box-sizing: border-box; margin: 0; padding: 0; }
  html, body { width: 1200px; height: 1000px; overflow: hidden; }
  body {
    background: var(--page-bg);
    font-family: "Open Sans", Arial, sans-serif;
    position: relative;
  }
  .card {
    position: absolute;
    left: 190px;
    width: 820px;
    height: 469px;
    overflow: hidden;
    box-shadow: 0 6px 18px rgba(0,0,0,0.18);
  }

  /* Back of card */
  .card-back {
    top: 20px;
    background: radial-gradient(ellipse at 45% 40%, var(--brand-blue-light) 0%, var(--brand-blue) 45%, var(--brand-blue-dark) 100%);
    color: var(--white);
  }
  .back-lockup {
    position: absolute;
    left: 50%;
    top: 50%;
    transform: translate(-50%, -50%);
    display: flex;
    align-items: center;
    gap: 20px;
    white-space: nowrap;
  }
  .back-lockup .mark-square { width: 46px; height: 46px; background: var(--white); flex: none; }
  .back-lockup .wordmark {
    font-family: "Questrial", Arial, sans-serif;
    font-size: 72px;
    line-height: 1;
    color: var(--white);
  }

  /* Front of card */
  .card-front {
    top: 511px;
    background: var(--white);
  }
  .portrait {
    position: absolute;
    left: 30px;
    top: 40px;
    width: 340px;
    height: 332px;
    background: linear-gradient(180deg, var(--photo-top) 0%, var(--photo-top) 35%, var(--photo-bottom) 100%);
  }
  .front-graphics { position: absolute; inset: 0; width: 820px; height: 469px; }
  .motto {
    position: absolute;
    left: 22px;
    top: 382px;
    font-size: 18px;
    line-height: 28px;
    color: var(--white);
    white-space: nowrap;
  }
  .front-info {
    position: absolute;
    right: 34px;
    top: 58px;
    width: 400px;
    text-align: right;
  }
  .front-lockup {
    display: flex;
    justify-content: flex-end;
    align-items: center;
    gap: 14px;
    white-space: nowrap;
  }
  .front-lockup .mark-square { width: 38px; height: 38px; background: var(--brand-blue); flex: none; }
  .front-lockup .wordmark {
    font-family: "Questrial", Arial, sans-serif;
    font-size: 56px;
    line-height: 1;
    color: var(--ink);
  }
  .person-name {
    margin-top: 62px;
    font-size: 23px;
    font-weight: 700;
    letter-spacing: 0.5px;
    color: var(--brand-blue);
  }
  .person-title {
    font-size: 18px;
    color: var(--sky);
    margin-top: 2px;
  }
  .info-rule {
    margin: 16px 0 14px auto;
    width: 210px;
    height: 1px;
    background: linear-gradient(90deg, transparent, var(--rule-grey));
  }
  .contact-list { list-style: none; }
  .contact-list li {
    display: flex;
    justify-content: flex-end;
    align-items: center;
    gap: 10px;
    font-size: 17px;
    line-height: 28px;
    color: var(--ink);
  }
  .contact-list svg { width: 16px; height: 16px; flex: none; }
</style>
</head>
<body>

  <section class="card card-back" aria-label="Card back">
    <div class="back-lockup">
      <span class="mark-square"></span>
      <span class="wordmark">LX Vantage</span>
    </div>
  </section>

  <section class="card card-front" aria-label="Card front">
    <div class="portrait" role="img" aria-label="Portrait photo of Marlene Okafor in a blue jacket"></div>

    <svg class="front-graphics" viewBox="0 0 820 469" aria-hidden="true">
      <polygon points="0,372 360,372 388,412 0,412" fill="var(--gold)"/>
      <polygon points="0,412 388,412 580,436 580,444 0,430" fill="var(--gold)"/>
      <rect x="590" y="426" width="24" height="24" fill="var(--sky)"/>
      <rect x="624" y="446" width="196" height="23" fill="var(--brand-blue)"/>
    </svg>
    <div class="motto">Develop your Rent Roll to Perform</div>

    <div class="front-info">
      <div class="front-lockup">
        <span class="mark-square"></span>
        <span class="wordmark">LX Vantage</span>
      </div>
      <div class="person-name">MARLENE OKAFOR</div>
      <div class="person-title">Property Management Consultant</div>
      <div class="info-rule"></div>
      <ul class="contact-list">
        <li>+61 438902716
          <svg viewBox="0 0 16 16"><path d="M3.5 1.5l2.5 0.5 1 3-1.6 1.2a9 9 0 0 0 4.4 4.4L11 9l3 1 0.5 2.5-2 2A11 11 0 0 1 1.5 3.5z" fill="var(--sky)"/></svg>
        </li>
        <li>marlene@lxvantage.com.au
          <svg viewBox="0 0 16 16"><rect x="1" y="3" width="14" height="10" fill="var(--sky)"/><path d="M1 3l7 6 7-6" fill="none" stroke="var(--white)" stroke-width="1.3"/></svg>
        </li>
        <li>www.lxvantage.com.au
          <svg viewBox="0 0 16 16"><circle cx="8" cy="8" r="7" fill="var(--sky)"/><path d="M1 8h14M8 1v14M8 1c-3 3-3 11 0 14M8 1c3 3 3 11 0 14" fill="none" stroke="var(--white)" stroke-width="1"/></svg>
        </li>
      </ul>
    </div>
  </section>

</body>
</html>
```